SOC audit and security advisory company

We are a small public accounting firm that specializes in SOC attestations for small to medium sized business throughout the U.S. Our business is much like consulting, but we form an opinion about their operational controls. We are looking for "relevance and with a hint of polished sophistication". Our logo colors are dark gray and red. Our existing site is www.veltrocheck.com for detailed information. We would like to include some type of captcha if possible. This is an information only site.

Target Market(s)

Small to medium sized financial and IT audit companies that are innovative and flexible.

Industry/Entity Type

Auditing

Coding

Coded - Design and coding required

Number of Pages Required

4 page

Font styles to use
Sans Serif

Requirements
Must have
• Good flow and attention to the content.
Nice to have
• CAPTCHA for contact us page
Should not have
• Big Bold lines.
• Too many distractions.

```html
<!DOCTYPE html>
<html lang="en">
<head>
<meta charset="utf-8">
<title>Veltro Audit &amp; Advisory</title>
<link href="https://fonts.googleapis.com/css2?family=Raleway:wght@300;400;500&family=Open+Sans:wght@400;600&display=swap" rel="stylesheet">
<style>
:root{
  --accent:#ee5128;
  --accent-deep:#d8391a;
  --green:#7ab648;
  --charcoal:#3a3a3a;
  --ink:#333;
  --muted:#6f6f6f;
  --rule:#d9d9d9;
  --footer:#e6e6e6;
  --white:#fff;
}
*{margin:0;padding:0;box-sizing:border-box}
html,body{width:747px;height:1200px;overflow:hidden;background:var(--white)}
body{position:relative;font-family:"Open Sans",sans-serif;color:var(--ink)}
.abs{position:absolute}

.site-header{left:0;top:0;width:747px;height:70px;background:var(--white)}
.brand{left:110px;top:27px;display:flex;align-items:center;gap:6px;font-family:"Raleway",sans-serif;font-size:12px;font-weight:500;color:var(--charcoal);white-space:nowrap}
.brand-dot{width:9px;height:9px;border-radius:50%;background:var(--accent)}
.nav{left:306px;top:0;height:70px;display:flex;font-family:"Raleway",sans-serif;font-size:9.5px;font-weight:500}
.nav a{color:var(--ink);text-decoration:none;height:70px;line-height:75px;padding:0 11px}
.nav a.active{background:var(--accent);color:var(--white);width:49px;padding:0;text-align:center}

.hero{left:0;top:70px;width:747px;height:298px;background:linear-gradient(90deg,#3b3b3b 0%,#545454 45%,#6b6b6b 75%,#4a4a4a 100%)}
.hero-title{left:94px;top:154px;font-family:"Raleway",sans-serif;font-weight:300;font-size:25px;line-height:30px;color:var(--white)}
.hero-sub{left:94px;top:186px;font-family:"Raleway",sans-serif;font-weight:400;font-size:15px;line-height:18px;color:var(--white)}
.hero-text{left:95px;top:211px;width:230px;font-size:8.2px;line-height:14px;color:#eee}
.dots{left:96px;top:252px;display:flex;gap:3px}
.dots span{width:10px;height:10px;border-radius:50%;background:#cfcfcf}
.dots span.on{background:#9aa64a;border:1px solid #cfcfcf}

.service{top:395px;width:180px;height:60px}
.service .icon{position:absolute;left:0;top:0;width:60px;height:60px;border-radius:50%;display:flex;align-items:center;justify-content:center}
.service h3{position:absolute;left:67px;top:7px;font-family:"Raleway",sans-serif;font-weight:500;font-size:10.5px;color:var(--ink)}
.service p{position:absolute;left:67px;top:25px;width:120px;font-size:6.3px;line-height:10.5px;color:var(--muted)}

.divider{left:94px;top:482px;width:559px;height:1px;background:var(--rule)}

.about-title{left:95px;top:510px;font-family:"Raleway",sans-serif;font-weight:300;font-size:20px;color:var(--ink)}
.about-text{left:95px;top:543px;width:292px;font-size:7.3px;line-height:12px;color:var(--muted)}
.about-text p{margin-bottom:7px}
.btn{left:94px;top:632px;width:72px;height:20px;background:#2e2e2e;color:var(--white);font-size:7.5px;line-height:20px;text-align:center;border-radius:2px;font-family:"Raleway",sans-serif;font-weight:500}
.about-photo{left:413px;top:515px;width:240px;height:139px;background:linear-gradient(135deg,#cfd3d6,#8e9499 60%,#4a4f55)}

.band{left:0;top:693px;width:747px;height:225px;background:linear-gradient(120deg,var(--accent-deep) 0%,var(--accent) 55%,#e8471f 100%)}
.card{top:727px;width:178px;height:161px;background:linear-gradient(#fff,#ececec)}
.card .photo{height:90px}
.card .notch{position:absolute;left:77px;top:80px;width:24px;height:12px;background:#fff;border-radius:12px 12px 0 0;text-align:center}
.card h4{position:absolute;top:100px;width:100%;text-align:center;font-family:"Raleway",sans-serif;font-weight:500;font-size:10.5px;color:var(--ink)}
.card p{position:absolute;top:116px;left:16px;width:146px;text-align:center;font-size:6.8px;line-height:12px;color:var(--muted)}
.card .more{position:absolute;top:142px;width:100%;text-align:center;font-size:7px;color:var(--accent);font-family:"Raleway",sans-serif;font-weight:500}

.advisors-title{left:0;top:938px;width:747px;text-align:center;font-family:"Raleway",sans-serif;font-weight:500;font-size:12px;color:var(--ink)}
.advisor{top:964px;width:120px;text-align:center}
.advisor .avatar{width:88px;height:88px;margin:0 auto;border-radius:50%;border:2px solid #ddd}
.advisor h5{margin-top:11px;font-family:"Raleway",sans-serif;font-weight:500;font-size:9.5px;color:var(--ink)}
.advisor p{margin-top:3px;font-size:7px;line-height:12px;color:var(--muted)}

.site-footer{left:0;top:1132px;width:747px;height:68px;background:var(--footer)}
.foot-nav{left:97px;top:1153px;display:flex;gap:22px;font-family:"Raleway",sans-serif;font-weight:500;font-size:9px;color:var(--ink)}
.copyright{left:97px;top:1171px;font-size:6.8px;color:var(--muted)}
.social{left:570px;top:1148px;display:flex;gap:2px}
.social span{width:18px;height:18px;border-radius:50%;border:1.3px solid #555}
</style>
</head>
<body>

<header class="site-header abs">
  <div class="brand abs"><span class="brand-dot"></span>Veltro Audit &amp; Advisory</div>
  <nav class="nav abs">
    <a class="active">HOME</a><a>ABOUT US</a><a>ADVISORY SERVICES</a><a>LINKS</a><a>CONTACT</a>
  </nav>
</header>

<section class="hero abs" role="img" aria-label="Smiling auditor working at a desk with binders and a calculator"></section>
<h1 class="hero-title abs">WE ARE SOC AUDIT</h1>
<h2 class="hero-sub abs">AND SECURITY ADVISORY</h2>
<p class="hero-text abs">Mauris vel lacus vitae felis vestibulum volutpat imperdiet ac nisl Cum sociis natoque penatibus et magnis</p>
<div class="dots abs"><span class="on"></span><span></span><span></span><span></span></div>

<div class="service abs" style="left:99px">
  <div class="icon" style="background:var(--charcoal)">
    <svg width="26" height="28" viewBox="0 0 26 28" fill="none" stroke="#fff" stroke-width="1.6"><path d="M13 2 L23 6 V13 C23 20 18 24 13 26 C8 24 3 20 3 13 V6 Z"/><path d="M8.5 14 L12 17.5 L18 10.5"/></svg>
  </div>
  <h3>Security Advisory</h3>
  <p>Lorem ipsum dolor sit amet consectet uer adipiscing elit Nam cursus Morbi ut malesuada iaculis ipsum dui</p>
</div>
<div class="service abs" style="left:290px">
  <div class="icon" style="background:var(--green)">
    <svg width="28" height="28" viewBox="0 0 28 28" fill="none" stroke="#fff" stroke-width="1.6"><rect x="4" y="3" width="15" height="20" rx="1"/><circle cx="16" cy="15" r="5"/><path d="M19.5 18.5 L25 24"/><path d="M7 8h9M7 12h4"/></svg>
  </div>
  <h3>SOC Attestations</h3>
  <p>Lorem ipsum dolor sit amet consectet uer adipiscing elit Nam cursus Morbi ut malesuada iaculis ipsum dui</p>
</div>
<div class="service abs" style="left:475px">
  <div class="icon" style="background:var(--accent)">
    <svg width="26" height="28" viewBox="0 0 26 28" fill="none" stroke="#fff" stroke-width="1.5"><rect x="4" y="3" width="17" height="22" rx="1"/><path d="M7 9l1.5 1.5L11 8M7 15l1.5 1.5L11 14"/><path d="M13 9h5M13 15h5M7 21h11"/></svg>
  </div>
  <h3>Accounting &amp; Audit</h3>
  <p>Lorem ipsum dolor sit amet consectet uer adipiscing elit Nam cursus Morbi ut malesuada iaculis ipsum dui</p>
</div>

<div class="divider abs"></div>

<h2 class="about-title abs">About Veltro Audit &amp; Advisory</h2>
<div class="about-text abs">
  <p>Donec dictum lectus non odio Cras a ante vitae enim iaculis aliquam Mauris nunc quam venenatis nec euismod sit amet egestas placerat est</p>
  <p>Cum sociis natoque penatibus et magnis dis parturient montes nascetur ridiculus mus In iaculis facilisis massa Etiam eu urna Sed porta Suspendisse quam leo molestie sed luctus quis feugiat in pede Fusce tellus Sed metus augue convallis et vehicula ut pulvinar eu ante Integer orci tellus tristique vitae consequat nec porta vel lec</p>
</div>
<div class="btn abs">READ MORE &rsaquo;</div>
<div class="about-photo abs" role="img" aria-label="Overhead view of an accountant using a calculator at a desk"></div>

<section class="band abs"></section>
<div class="card abs" style="left:94px">
  <div class="photo" role="img" aria-label="Colourful bar chart on a glass screen" style="background:linear-gradient(120deg,#e9e9e9,#c9c9c9 50%,#b8b0c8)"></div>
  <div class="notch"><svg width="12" height="8" viewBox="0 0 12 8"><path d="M2 2 L6 6 L10 2" fill="none" stroke="#888" stroke-width="1.2"/></svg></div>
  <h4>WHY CHOOSE US</h4>
  <p>Fusce tellus Sed metus augue convallis et vehicula ut pulvinar eu ante Integer</p>
  <div class="more">READ MORE</div>
</div>
<div class="card abs" style="left:284px">
  <div class="photo" role="img" aria-label="Businessman working with a calculator and papers" style="background:linear-gradient(135deg,#9aa0a6,#4c5258 60%,#2e3236)"></div>
  <div class="notch"><svg width="12" height="8" viewBox="0 0 12 8"><path d="M2 2 L6 6 L10 2" fill="none" stroke="#888" stroke-width="1.2"/></svg></div>
  <h4>OUR TEAM</h4>
  <p>Fusce tellus Sed metus augue convallis et vehicula ut pulvinar eu ante Integer</p>
  <div class="more">READ MORE</div>
</div>
<div class="card abs" style="left:474px">
  <div class="photo" role="img" aria-label="Group of business people meeting in an office" style="background:linear-gradient(135deg,#b38a4e,#5a4a3c 55%,#2f2f36)"></div>
  <div class="notch"><svg width="12" height="8" viewBox="0 0 12 8"><path d="M2 2 L6 6 L10 2" fill="none" stroke="#888" stroke-width="1.2"/></svg></div>
  <h4>FREE CONSULTATION</h4>
  <p>Fusce tellus Sed metus augue convallis et vehicula ut pulvinar eu ante Integer</p>
  <div class="more">READ MORE</div>
</div>

<h2 class="advisors-title abs">OUR ADVISORS</h2>
<div class="advisor abs" style="left:107px">
  <div class="avatar" role="img" aria-label="Advisor portrait" style="background:radial-gradient(circle at 50% 40%,#b9a08a,#8a8f96)"></div>
  <h5>Member Name</h5><p>Fusce tellus Sed metus augue<br>convallis et vehicula</p>
</div>
<div class="advisor abs" style="left:241px">
  <div class="avatar" role="img" aria-label="Advisor portrait" style="background:radial-gradient(circle at 50% 40%,#a88469,#6f8fb4)"></div>
  <h5>Member Name</h5><p>Fusce tellus Sed metus augue<br>convallis et vehicula</p>
</div>
<div class="advisor abs" style="left:374px">
  <div class="avatar" role="img" aria-label="Advisor portrait" style="background:radial-gradient(circle at 50% 40%,#b79a86,#3a3d44)"></div>
  <h5>Member Name</h5><p>Fusce tellus Sed metus augue<br>convallis et vehicula</p>
</div>
<div class="advisor abs" style="left:507px">
  <div class="avatar" role="img" aria-label="Advisor portrait" style="background:radial-gradient(circle at 50% 40%,#c49d84,#6a5a50)"></div>
  <h5>Member Name</h5><p>Fusce tellus Sed metus augue<br>convallis et vehicula</p>
</div>

<footer class="site-footer abs"></footer>
<div class="foot-nav abs"><span>HOME</span><span>ABOUT US</span><span>ADVISORY SERVICES</span><span>LINKS</span><span>CONTACT</span></div>
<div class="copyright abs">© 2016 Company Name &nbsp;All right reserved &nbsp;Term of Use</div>
<div class="social abs"><span></span><span></span><span></span><span></span></div>

</body>
</html>
```